Photography business - business card design quick turn around

Create a business card design for me please. I actually need the final design back before the end of Sunday 13th May 7pm GMT. Sorry for the short notice.

Photoshop artwork template uploaded with artwork guidelines including printer profiles and other mandatory specifications. Only one side of the business card is required as the other side will be an image.

The design is required as an unflattened PSD file so that I can edit the text if I need to.

My brand colours are white and the teal you see in the logo. Occasionally I also use a dark grey on my website (I don't mind the shade of grey as appreciate grey on teal would be a different grey, to the grey I use on white on the website, so just use a shade of grey that matches). Font can be as the font for the logo or if you prefer I am open to another sans serif, easily legible font. Ideally font size will be 12+.Please do not use capital letters for text. I prefer everything to be lower case, if possible.

Thank you.

Mira

Target Market(s)

Other business owners who may refer me and families

Industry/Entity Type

Photographer

Contact Information for Business Card

Silver Lantern Photography Logo
Sub text: family portraiture, captured with love

Contact information, ideally using simple icons to represent email / website / facebook / instagram / pinterest

email: mira@silverlanternphotography.co.uk
website: silverlanternphotography.co.uk
facebook: @silverlanternphotography
pinterest: pinterest.com/silverlanternph
instagram: @silverlantern_photography
mobile/telephone: 07931460217

If there is too much text then please drop the instagram and pinterest information.

Font styles to use
Sans Serif

Colors
33b8a4

Requirements
Must have
• Logo
• Contact details as listed above
• sub text
Nice to have
• Instagram and Pinterest contact details
• Nice to have icons to represent website / phone / facebook etc followered by the handle where relevant

```html
<!DOCTYPE html>
<html lang="en">
<head>
<meta charset="utf-8">
<title>silver lantern photography – business card</title>
<link rel="stylesheet" href="https://fonts.googleapis.com/css2?family=Arimo:wght@400&family=Crimson+Text:ital@1&display=swap">
<style>
  :root {
    --backdrop: #1e1e1f;
    --brand-teal: #33b8a4;
    --brand-teal-deep: #2aa391;
    --band-grey: #3d4443;
    --panel-white: #ffffff;
    --panel-shade: #ececec;
    --ink: #2e3433;
    --on-teal: #ffffff;
    --tagline: #e8f6f3;
  }
  * { box-sizing: border-box; margin: 0; padding: 0; }
  html, body {
    width: 1200px; height: 997px; overflow: hidden;
    background: var(--backdrop);
  }
  .business-card {
    position: absolute; left: 180px; top: 258px;
    width: 840px; height: 480px;
    border-radius: 28px; overflow: hidden;
    background: linear-gradient(135deg, var(--brand-teal), var(--brand-teal-deep));
  }
  .contact-panel {
    position: absolute; inset: 0;
    background: linear-gradient(160deg, var(--panel-white) 30%, var(--panel-shade));
    clip-path: polygon(0 0, 46% 0, 60% 100%, 0 100%);
  }
  .tagline-band {
    position: absolute; left: 0; right: 0; top: 345px; height: 62px;
    background: var(--band-grey);
    display: flex; align-items: center; padding-left: 40px;
  }
  .tagline {
    font-family: "Crimson Text", Georgia, serif; font-style: italic;
    font-size: 27px; color: var(--tagline); letter-spacing: 0.5px;
  }
  .contact-list {
    position: absolute; left: 38px; top: 92px; list-style: none;
    font-family: "Arimo", Arial, sans-serif; font-size: 17px; color: var(--ink);
  }
  .contact-item { display: flex; align-items: center; height: 36px; }
  .contact-icon { width: 15px; height: 15px; margin-right: 12px; flex: none; }
  .brand-name {
    position: absolute; left: 470px; top: 148px; width: 340px;
    font-family: "Arimo", Arial, sans-serif; font-weight: 400;
    color: var(--on-teal); text-align: center; line-height: 1.15;
  }
  .brand-name .brand-line { display: block; font-size: 34px; letter-spacing: 1px; }
  .brand-name .brand-sub { display: block; font-size: 20px; letter-spacing: 4px; }
</style>
</head>
<body>
  <div class="business-card">
    <div class="contact-panel"></div>

    <ul class="contact-list">
      <li class="contact-item">
        <svg class="contact-icon" viewBox="0 0 16 16" aria-hidden="true"><path fill="#33b8a4" d="M2 2h12a1 1 0 0 1 1 1v8a1 1 0 0 1-1 1H7l-4 3v-3H2a1 1 0 0 1-1-1V3a1 1 0 0 1 1-1z"/></svg>
        silverlanternphotography
      </li>
      <li class="contact-item">
        <svg class="contact-icon" viewBox="0 0 16 16" aria-hidden="true"><path fill="#33b8a4" d="M4 1h8a1 1 0 0 1 1 1v13l-5-3-5 3V2a1 1 0 0 1 1-1z"/></svg>
        silverlanternph
      </li>
      <li class="contact-item">
        <svg class="contact-icon" viewBox="0 0 16 16" aria-hidden="true"><path fill="#33b8a4" d="M8 14.5S1 10.3 1 5.6A3.6 3.6 0 0 1 8 4a3.6 3.6 0 0 1 7 1.6c0 4.7-7 8.9-7 8.9z"/></svg>
        silverlantern_photography
      </li>
      <li class="contact-item">
        <svg class="contact-icon" viewBox="0 0 16 16" aria-hidden="true"><path fill="#33b8a4" d="M3 1h3l1.5 4-2 1.3a9 9 0 0 0 4.2 4.2l1.3-2 4 1.5v3c0 1-1 2-2 2A13 13 0 0 1 1 3c0-1 1-2 2-2z"/></svg>
        07931460217
      </li>
      <li class="contact-item">
        <svg class="contact-icon" viewBox="0 0 16 16" aria-hidden="true"><rect x="1" y="3" width="14" height="10" rx="1.5" fill="#33b8a4"/><path d="M1.5 4l6.5 5 6.5-5" stroke="#fff" stroke-width="1.3" fill="none"/></svg>
        mira@silverlanternphotography.co.uk
      </li>
      <li class="contact-item">
        <svg class="contact-icon" viewBox="0 0 16 16" aria-hidden="true"><path fill="#33b8a4" d="M8 1a5 5 0 0 1 5 5c0 4-5 9-5 9S3 10 3 6a5 5 0 0 1 5-5z"/><circle cx="8" cy="6" r="1.8" fill="#fff"/></svg>
        silverlanternphotography.co.uk
      </li>
    </ul>

    <div class="brand-name">
      <span class="brand-line">silver lantern</span>
      <span class="brand-sub">photography</span>
    </div>

    <div class="tagline-band">
      <p class="tagline">family portraiture, captured with love</p>
    </div>
  </div>
</body>
</html>
```